Business Card Design for Event Planning Company

Create a business card for event planning company using our new logo. After I pick the design, I will need files made for 6 employees. Our company provides event design & logistics services as well as venue management. The font should be sans serif and complementary to the logo. I will need to know the name of the font selected for the final design. The phone numbers listed should be separated by "." not "-"

Address for the card
PO Box 318, Washington, DC 20019

Card One
Lorna Pettibone
lpettibone@galavoyant.com
202.481.7730

Card Two
Miriam Okonkwo
mokonkwo@galavoyant.com
202.556.2047

Card Three
Tessa Varnholt
tvarnholt@galavoyant.com
978.620.4471

Card Four
Robin Fess
rfess@galavoyant.com
202.718.3362

Card Five
Ada-Rose Pelletan-Uzor
adarose@galavoyant.com
202.839.1205

Card Six
Beatrix Holloway
Beatrix@galavoyant.com
202.492.6618

Target Market(s)

Corporate/Non-Profit

Industry/Entity Type

Event Planning

Contact Information for Business Card

Address for the card

Card One
Lorna Pettibone
lpettibone@galavoyant.com
202.481.7730

Card Two
Miriam Okonkwo
202.556.2047

Card Three
Tessa Varnholt
978.620.4471

Card Four
Robin Fess
rfess@galavoyant.com
202.718.3362

Card Five
Ada-Rose Pelletan-Uzor
202.839.1205

Card Six
Beatrix Holloway
202.492.6618

Font styles to use
Sans Serif

Colors

Designer to choose colors to be used in the design.

Requirements
Must have
• Two-sided with logo
Should not have
• Extra colors or be too busy

```html
<!DOCTYPE html>
<html lang="en">
<head>
<meta charset="utf-8">
<title>Galavoyant — Business Card</title>
<link href="https://fonts.googleapis.com/css2?family=Questrial&display=swap" rel="stylesheet">
<style>
  :root {
    --teal: #62aaa5;
    --teal-deep: #579e99;
    --paper: #ffffff;
    --ink: #1b1b1b;
    --backdrop: #ececec;
  }
  * { margin: 0; padding: 0; box-sizing: border-box; }
  html, body {
    width: 1200px; height: 871px; overflow: hidden;
    background: var(--backdrop);
    font-family: "Questrial", "Century Gothic", sans-serif;
  }
  .stage {
    width: 1200px; height: 871px;
    display: flex; flex-direction: column;
    align-items: center; justify-content: center; gap: 40px;
  }
  .card {
    position: relative;
    width: 680px; height: 389px;
    background: var(--teal);
    overflow: hidden;
    box-shadow: 0 6px 18px rgba(0,0,0,0.12);
  }
  .card__disc {
    position: absolute;
    border-radius: 50%;
    background: var(--paper);
  }
  /* Front */
  .card--front .card__disc {
    width: 720px; height: 720px;
    left: -300px; top: -340px;
  }
  .contact-rail {
    position: absolute;
    left: 18px; top: 0; bottom: 0;
    width: 36px;
  }
  .contact {
    position: absolute;
    left: 80px; top: 44px;
    color: var(--ink);
  }
  .contact__name {
    font-size: 36px; letter-spacing: 1.5px; font-weight: 400;
    margin-bottom: 22px;
  }
  .contact__line {
    font-size: 19px; letter-spacing: 0.5px; line-height: 30px;
  }
  .contact__address { margin-top: 34px; }
  .front-brand {
    position: absolute;
    right: 44px; bottom: 44px;
    color: var(--paper);
    font-size: 40px; letter-spacing: 1px;
  }
  /* Back */
  .card--back .card__disc {
    width: 640px; height: 640px;
    left: 150px; top: -140px;
  }
  .brand {
    position: absolute;
    left: 235px; top: 160px;
    display: flex; align-items: center; gap: 18px;
  }
  .brand__name {
    font-size: 68px; color: var(--ink); letter-spacing: 1px;
  }
  .brand__dot {
    width: 22px; height: 22px; border-radius: 50%;
    background: var(--teal);
  }
</style>
</head>
<body>
<main class="stage">
  <section class="card card--front" aria-label="Card front with contact details">
    <div class="card__disc"></div>
    <svg class="contact-rail" viewBox="0 0 36 389" width="36" height="389" aria-hidden="true">
      <rect x="4" y="0" width="28" height="389" rx="14" fill="var(--teal)"/>
      <circle cx="18" cy="30" r="7" fill="#fff"/>
      <!-- phone -->
      <rect x="11" y="84" width="14" height="22" rx="2" fill="none" stroke="#fff" stroke-width="2"/>
      <line x1="15" y1="102" x2="21" y2="102" stroke="#fff" stroke-width="2"/>
      <!-- envelope -->
      <rect x="8" y="126" width="20" height="14" fill="#fff"/>
      <polyline points="8,126 18,134 28,126" fill="none" stroke="var(--teal)" stroke-width="2"/>
      <!-- pin -->
      <path d="M18 318 C11 318 8 323 8 327 C8 334 18 344 18 344 C18 344 28 334 28 327 C28 323 25 318 18 318 Z" fill="#fff"/>
      <circle cx="18" cy="327" r="3.5" fill="var(--teal)"/>
    </svg>
    <div class="contact">
      <p class="contact__name">Lorna Pettibone</p>
      <p class="contact__line">lpettibone@galavoyant.com</p>
      <p class="contact__line">202.481.7730</p>
      <p class="contact__line contact__address">PO Box 318,<br>Washington, DC 20019</p>
    </div>
    <p class="front-brand">galavoyant</p>
  </section>

  <section class="card card--back" aria-label="Card back with company name">
    <div class="card__disc"></div>
    <div class="brand">
      <span class="brand__name">galavoyant</span>
      <span class="brand__dot"></span>
    </div>
  </section>
</main>
</body>
</html>
```